I am a home builder and developer

I would like some sort of architectural design like a pencil type of drawing of a house but want it to be professional looking and two sided.

Simply I am a custom home builder and land developer. I would like a new design other than what I have now that's what I thought y'all did. I like mostly black maybe with an pencil type of drawing of a house. Like an architectural look.

Industry/Entity Type

Home Builder

```html
<!DOCTYPE html>
<html lang="en">
<head>
<meta charset="utf-8">
<title>Harmon Estate – Business Card</title>
<link rel="stylesheet" href="https://fonts.googleapis.com/css2?family=Lato:wght@300;400;700;900&display=swap">
<style>
  :root {
    --backdrop: #0e0e0e;
    --paper: #ffffff;
    --ink: #2b2828;
    --ink-soft: #3a3737;
    --accent: #0a8fd6;
    --photo-sky: #dfe8d2;
    --photo-house: #c9c2b8;
    --sketch: #eeeeee;
  }
  * { margin: 0; padding: 0; box-sizing: border-box; }
  html, body {
    width: 1200px; height: 1200px; overflow: hidden;
    background: var(--backdrop);
    font-family: "Lato", sans-serif;
  }
  .sheet {
    width: 1200px; height: 1200px;
    display: flex; flex-direction: column;
    align-items: center; justify-content: center; gap: 44px;
  }
  .card {
    position: relative;
    width: 900px; height: 514px;
    background: var(--paper);
    overflow: hidden;
  }
  .card svg.art { position: absolute; inset: 0; }

  /* Front */
  .brand {
    position: absolute; left: 70px; top: 62px;
    display: flex; align-items: center; gap: 18px;
  }
  .brand-dot {
    width: 58px; height: 58px; border-radius: 50%;
    background: var(--accent);
  }
  .brand-name {
    font-weight: 300; font-size: 44px; letter-spacing: 1px;
    color: var(--ink);
  }
  .contacts {
    position: absolute; left: 70px; top: 168px;
    list-style: none;
  }
  .contact {
    display: flex; align-items: flex-start; gap: 20px;
    margin-bottom: 14px;
  }
  .contact-icon {
    flex: none; width: 34px; height: 34px;
    border: 2px solid var(--accent); border-radius: 50%;
    display: flex; align-items: center; justify-content: center;
  }
  .contact-text {
    font-size: 22px; line-height: 27px; color: var(--ink);
    font-weight: 400;
  }
  .person-name { font-size: 32px; line-height: 32px; color: var(--ink); }
  .person-name b { font-weight: 900; }
  .person-name span { font-weight: 300; }
  .person-role {
    font-size: 19px; letter-spacing: 0.5px; color: var(--accent);
    font-weight: 400; text-transform: uppercase;
  }

  /* Back */
  .back-brand {
    position: absolute; right: 70px; bottom: 60px;
    font-weight: 300; font-size: 44px; letter-spacing: 1px;
    line-height: 1;
    color: var(--ink);
  }
</style>
</head>
<body>
<main class="sheet">

  <section class="card card-front" aria-label="Card front">
    <svg class="art" viewBox="0 0 900 514" width="900" height="514">
      <defs>
        <linearGradient id="photoTone" x1="0" y1="0" x2="1" y2="1">
          <stop offset="0" stop-color="var(--photo-sky)"/>
          <stop offset="0.55" stop-color="var(--photo-house)"/>
          <stop offset="1" stop-color="#6c6a5e"/>
        </linearGradient>
      </defs>
      <polygon class="stripe-dark" points="555,300 575,514 625,514" fill="var(--ink)"/>
      <polygon class="stripe-blue" points="585,255 645,514 700,514" fill="var(--accent)"/>
      <polygon class="photo-frame" points="545,190 900,220 900,290 760,514 695,514" fill="var(--ink)"/>
      <polygon class="photo" role="img" aria-label="Photograph of a two-storey white house with tiled roof"
               points="575,208 900,237 900,285 760,514 712,514" fill="url(#photoTone)"/>
    </svg>

    <div class="brand">
      <div class="brand-dot"></div>
      <div class="brand-name">HARMON ESTATE</div>
    </div>

    <ul class="contacts">
      <li class="contact">
        <span class="contact-icon">
          <svg width="18" height="18" viewBox="0 0 18 18"><circle cx="9" cy="6" r="3.5" fill="var(--accent)"/><path d="M2 17c0-4 3-6.5 7-6.5s7 2.5 7 6.5z" fill="var(--accent)"/></svg>
        </span>
        <div>
          <div class="person-name"><b>DALE</b> <span>HARMON</span></div>
          <div class="person-role">Real Estate Agent</div>
        </div>
      </li>
      <li class="contact">
        <span class="contact-icon">
          <svg width="18" height="18" viewBox="0 0 18 18"><path d="M4 2l3 3-1.5 2c1 2 3 4 5 5l2-1.5 3 3-2 2C8 15 3 10 2 4z" fill="none" stroke="var(--accent)" stroke-width="1.6"/></svg>
        </span>
        <div class="contact-text">555 . 201. 4410<br>555 . 201. 4411</div>
      </li>
      <li class="contact">
        <span class="contact-icon">
          <svg width="18" height="18" viewBox="0 0 18 18" fill="none" stroke="var(--accent)" stroke-width="1.4"><circle cx="9" cy="9" r="7"/><ellipse cx="9" cy="9" rx="3" ry="7"/><line x1="2" y1="9" x2="16" y2="9"/></svg>
        </span>
        <div class="contact-text">info@harmonhomes.com<br>www.harmonhomes.com</div>
      </li>
      <li class="contact">
        <span class="contact-icon">
          <svg width="18" height="18" viewBox="0 0 18 18"><path d="M9 17s-5-6-5-10a5 5 0 0 1 10 0c0 4-5 10-5 10z" fill="none" stroke="var(--accent)" stroke-width="1.6"/><circle cx="9" cy="7" r="1.8" fill="var(--accent)"/></svg>
        </span>
        <div class="contact-text">Cedar Ridge Lane 14<br>Texas 78701 - United States</div>
      </li>
    </ul>
  </section>

  <section class="card card-back" aria-label="Card back">
    <svg class="art" viewBox="0 0 900 514" width="900" height="514">
      <defs>
        <linearGradient id="shade" x1="0" y1="0" x2="0" y2="1">
          <stop offset="0" stop-color="#d9d9d9"/>
          <stop offset="0.4" stop-color="#ffffff"/>
        </linearGradient>
      </defs>
      <rect width="900" height="514" fill="url(#shade)" opacity="0.6"/>
      <polygon class="sketch" role="img" aria-label="Pencil architectural elevation drawing of a house"
               points="140,0 900,0 900,290" fill="var(--sketch)"/>
      <polygon class="band-dark" points="95,0 140,0 900,290 900,320" fill="var(--ink)"/>
      <polygon class="band-blue" points="40,0 80,0 900,342 900,362" fill="var(--accent)"/>
      <polygon class="band-dark-thin" points="0,10 0,45 720,330" fill="var(--ink-soft)"/>
    </svg>
    <div class="back-brand">HARMON ESTATE</div>
  </section>

</main>
</body>
</html>
```